Homebrew-webshop picture design

I need help with catogory-pics and frontpage-pics for my homebrew-webshop: http://skovbakkendk.stage58.webtuplo.dk/

My main buiness is raw materials and equipment for small scale beer-brewing.
I would like the pics is welcoming and descriptive.
Cues: Quality products, Customer Care, Personal service,

```html
<!DOCTYPE html>
<html lang="en">
<head>
<meta charset="utf-8">
<title>Kornlyst.dk – Homebrew webshop</title>
<link href="https://fonts.googleapis.com/css2?family=Lora:wght@400;700&family=Roboto:wght@300;400;500;700&display=swap" rel="stylesheet">
<style>
:root{
  --navy:#0b3566;
  --blue:#1565c0;
  --blue-dark:#0e4a91;
  --ink:#222;
  --muted:#777;
  --line:#dde3ea;
  --pale:#eef4fb;
  --red:#e53935;
  --white:#fff;
  --footer:#f4f4f4;
}
*{box-sizing:border-box;margin:0;padding:0}
html,body{width:1200px;height:3168px;overflow:hidden}
body{font-family:"Roboto",Arial,sans-serif;color:var(--ink);background:var(--white);position:relative}
a{color:inherit;text-decoration:none}

.topbar{height:40px;background:var(--navy);color:#fff;display:flex;justify-content:center;gap:70px;align-items:center;font-size:13px;font-weight:500;letter-spacing:.5px}
.header{height:72px;display:flex;align-items:center;padding:0 140px;gap:40px}
.brand{font-family:"Lora",serif;font-weight:700;font-size:30px;color:var(--navy);white-space:nowrap}
.search{display:flex;margin-left:40px}
.search input{width:230px;height:34px;border:1px solid var(--line);padding:0 12px;font-size:13px;font-family:inherit}
.search button{width:36px;height:34px;background:var(--navy);border:0;display:flex;align-items:center;justify-content:center}
.account{margin-left:auto;text-align:right;font-size:12px;color:var(--muted)}
.account .phone{font-size:22px;font-weight:700;color:var(--navy);display:flex;align-items:center;gap:6px}
.cart{display:flex;align-items:center;gap:10px;font-size:12px;color:var(--ink)}
.cart .bag{width:46px;height:46px;border-radius:50%;background:var(--navy);display:flex;align-items:center;justify-content:center}
.nav{height:40px;background:#f1f1f1;border-top:1px solid var(--line);display:flex;padding:0 140px;font-size:13px;font-weight:500}
.nav a{padding:0 16px;display:flex;align-items:center}
.nav a.active{background:var(--blue);color:#fff}
.hero{position:relative;height:608px;overflow:hidden}
.hero-photo{position:absolute;inset:0;background:linear-gradient(100deg,#2c3a46 0%,#6d7b86 30%,#a9b3ba 55%,#7d8a93 80%,#3f4b55 100%)}
.hero-text{position:absolute;left:140px;top:190px;color:#fff}
.hero-text h1{font-family:"Lora",serif;font-size:54px;font-weight:700;letter-spacing:1px}
.hero-text p{font-size:20px;margin-top:6px}
.hero-cta{display:flex;align-items:center;gap:10px;margin-top:56px}
.code{background:var(--navy);font-size:34px;font-weight:700;padding:4px 18px}
.shop{background:var(--blue);font-size:14px;font-weight:700;padding:10px 18px;border-radius:3px}
.dots{position:absolute;left:50%;top:500px;transform:translateX(-50%);display:flex;gap:8px}
.dots span{width:10px;height:10px;border-radius:50%;background:#fff;opacity:.6}
.dots span:first-child{opacity:1}
.hero svg.curve{position:absolute;left:0;bottom:0}
.welcome{text-align:center;padding-top:70px}
.welcome h2{font-family:"Lora",serif;font-weight:400;font-size:40px;color:var(--ink)}
.welcome h2 span{color:var(--blue)}
.welcome p{width:860px;margin:44px auto 0;font-size:13px;line-height:25px;color:var(--muted)}
.categories{position:relative;display:flex;justify-content:center;gap:36px;margin-top:56px}
.cat{width:208px;text-align:center}
.cat .pic{width:208px;height:208px;border-radius:50%;border:6px solid #fff;box-shadow:0 2px 8px rgba(0,0,0,.18)}
.cat h3{margin-top:26px;font-size:15px;font-weight:700;line-height:20px}
.cat-arrow{position:absolute;top:86px}
.cues{display:flex;justify-content:center;gap:28px;margin-top:116px}
.cue{width:280px;height:112px;border:1px solid var(--line);display:flex;align-items:center;gap:18px;padding-left:22px;font-size:20px;font-weight:700;color:var(--navy)}
.cue .ico{width:50px;height:50px;border-radius:50%;background:var(--blue);display:flex;align-items:center;justify-content:center}
.featured{position:absolute;top:1720px;left:0;width:1200px;height:960px;background:var(--pale);text-align:center}
.featured h2{font-family:"Lora",serif;font-weight:400;font-size:40px;margin-top:100px;letter-spacing:1px}
.featured h2 span{color:var(--blue)}
.grid{display:grid;grid-template-columns:repeat(4,208px);gap:24px 32px;justify-content:center;margin-top:64px}
.card{background:#fff;height:284px;position:relative;padding:14px;box-shadow:0 1px 4px rgba(0,0,0,.08)}
.card .pic{height:150px;margin:0 12px}
.card .new{position:absolute;right:10px;top:8px;background:var(--red);color:#fff;font-size:10px;font-weight:700;padding:2px 6px}
.card h4{font-size:14px;font-weight:700;margin-top:14px}
.card .price{font-size:13px;color:var(--blue);margin-top:4px}
.card .add{display:inline-block;margin-top:12px;background:var(--blue-dark);color:#fff;font-size:10px;font-weight:700;padding:6px 12px;border-radius:3px}
.pager{display:flex;justify-content:center;gap:12px;margin-top:60px}
.pager span{width:36px;height:36px;border-radius:50%;border:1px solid #999;display:flex;align-items:center;justify-content:center}
.mailing{position:absolute;top:2700px;left:0;width:1200px;height:104px;background:var(--navy);display:flex;align-items:center;padding:0 140px;color:#fff}
.mailing h2{font-weight:300;font-size:36px;letter-spacing:1px}
.mailing input{margin-left:auto;width:360px;height:40px;border:0;padding:0 14px;font-size:14px;font-family:inherit}
.mailing button{width:128px;height:40px;background:#111d2e;color:#fff;border:0;font-weight:700;font-size:15px;font-family:inherit}
.footer{position:absolute;top:2804px;left:0;width:1200px;height:280px;background:var(--footer);display:grid;grid-template-columns:290px 250px 200px 200px;padding:40px 0 0 140px}
.footer h5{font-size:15px;font-weight:700;margin-bottom:16px}
.footer li{list-style:none;font-size:12px;color:#555;line-height:22px;display:flex;gap:8px;align-items:flex-start}
.footer li svg{margin-top:4px;flex:none}
.social{display:flex;gap:8px}
.social span{width:28px;height:28px;border-radius:50%;background:#8aa0b8}
.bottom{position:absolute;top:3084px;left:0;width:1200px;height:84px;border-top:1px solid var(--line);display:flex;align-items:center;padding:0 140px;gap:8px;font-size:12px;color:#666}
.paycard{width:46px;height:28px;border-radius:3px;background:#c9d1da}
.copy{margin-left:230px}
.totop{margin-left:auto;width:44px;height:44px;border-radius:50%;border:1px solid #999;display:flex;align-items:center;justify-content:center}
</style>
</head>
<body>

<div class="topbar">
  <span>SHIPPING ONLY $99.95</span>
  <span>FREE SHIPPING ON BUY OVER 500</span>
  <span>SECURE PAYMENT</span>
  <span>30 DAY RETURN POLICY</span>
</div>

<header class="header">
  <a class="brand" href="#">Kornlyst.dk</a>
  <form class="search">
    <input type="text" placeholder="Search">
    <button type="button" aria-label="Search"><svg width="16" height="16" viewBox="0 0 16 16"><circle cx="7" cy="7" r="5" fill="none" stroke="#fff" stroke-width="2"/><path d="M11 11l4 4" stroke="#fff" stroke-width="2"/></svg></button>
  </form>
  <div class="account">
    <div>HELP | LOG IN</div>
    <div class="phone"><svg width="16" height="16" viewBox="0 0 24 24"><path d="M6 2l4 4-2 3c1 3 4 6 7 7l3-2 4 4-3 4C10 21 3 14 2 5z" fill="#0b3566"/></svg>40 12 34 56</div>
  </div>
  <div class="cart">
    <span class="bag"><svg width="22" height="22" viewBox="0 0 24 24"><path d="M3 4h3l3 11h10l2-8H7" fill="none" stroke="#fff" stroke-width="2"/><circle cx="10" cy="19" r="1.6" fill="#fff"/><circle cx="17" cy="19" r="1.6" fill="#fff"/></svg></span>
    <span>View Cart<br>(0) Items</span>
  </div>
</header>

<nav class="nav">
  <a class="active" href="#">HOME</a>
  <a href="#">COMMODITIES</a>
  <a href="#">BREWING AND FERMENTATION</a>
  <a href="#">BOTTLING</a>
  <a href="#">CLEANING</a>
  <a href="#">LABORATORY</a>
  <a href="#">PARTS</a>
  <a href="#">BOOKS</a>
</nav>

<section class="hero">
  <div class="hero-photo" role="img" aria-label="Brewery interior with rows of steel fermentation tanks"></div>
  <div class="hero-text">
    <h1>NEWEST PRODUCTS</h1>
    <p>Lorem ipsum dolor sit consectetur adipiscing</p>
    <div class="hero-cta"><span class="code">F4275</span><a class="shop" href="#">SHOP NOW ›</a></div>
  </div>
  <div class="dots"><span></span><span></span><span></span><span></span><span></span></div>
  <svg class="curve" width="1200" height="70" viewBox="0 0 1200 70"><path d="M0 0 Q600 110 1200 0 L1200 70 L0 70Z" fill="#fff"/></svg>
</section>

<section class="welcome">
  <h2>Welcome to <span>Kornlyst.dk</span></h2>
  <p>Lorem ipsum dolor sit amet, consectetur adipiscing elit do eiusmod tempor incididunt ut labore et dolore na aliqua. Ipsum suspendisse ultrices gravida commodo viverra maecenas accumsan lacus vel facilisis nam ipsum dolor sit amet, consectetur adipiscing elit sed do eiusmod tempor incididunt ut labore et dolore ma aliqua quis suspendisse ultrices gravidasa commodo viverra maecenas accumsan lacus vel facilisis.</p>
</section>

<section class="categories">
  <svg class="cat-arrow" style="left:80px" width="20" height="36" viewBox="0 0 20 36"><path d="M18 2L2 18l16 16" fill="none" stroke="#bbb" stroke-width="2"/></svg>
  <div class="cat"><div class="pic" role="img" aria-label="Bowls of malted grain and hops" style="background:radial-gradient(circle,#a58a3c,#6d5a24)"></div><h3>COMMODITIES</h3></div>
  <div class="cat"><div class="pic" role="img" aria-label="Stainless brewing kettles and fermenter" style="background:radial-gradient(circle,#d7d9db,#6e7379)"></div><h3>BREWING AND<br>FERMENTATION</h3></div>
  <div class="cat"><div class="pic" role="img" aria-label="Bottle tree and capping tools" style="background:radial-gradient(circle,#e9e3dc,#a63a2c)"></div><h3>BOTTLING</h3></div>
  <div class="cat"><div class="pic" role="img" aria-label="Cleaning agents in containers" style="background:radial-gradient(circle,#fafafa,#c9cfd6)"></div><h3>CLEANING</h3></div>
  <svg class="cat-arrow" style="right:80px" width="20" height="36" viewBox="0 0 20 36"><path d="M2 2l16 16L2 34" fill="none" stroke="#bbb" stroke-width="2"/></svg>
</section>

<section class="cues">
  <div class="cue"><span class="ico"><svg width="26" height="26" viewBox="0 0 24 24"><path d="M2 10h4v11H2zM8 21V10l5-8c2 0 2 2 2 3l-1 4h6c1 0 2 1 2 2l-2 8c0 1-1 2-2 2z" fill="#fff"/></svg></span>Quality products</div>
  <div class="cue"><span class="ico"><svg width="26" height="26" viewBox="0 0 24 24"><path d="M4 14v-2a8 8 0 0116 0v2" fill="none" stroke="#fff" stroke-width="2"/><rect x="2" y="13" width="5" height="7" rx="1" fill="#fff"/><rect x="17" y="13" width="5" height="7" rx="1" fill="#fff"/></svg></span>Customer Care</div>
  <div class="cue"><span class="ico"><svg width="26" height="26" viewBox="0 0 24 24"><circle cx="12" cy="8" r="4.5" fill="#fff"/><path d="M3 22c0-5 4-8 9-8s9 3 9 8z" fill="#fff"/></svg></span>Personal service</div>
</section>

<section class="featured">
  <h2>FEATURED <span>PRODUCTS</span></h2>
  <div class="grid">
    <div class="card"><div class="pic" role="img" aria-label="Water dispenser container" style="background:linear-gradient(#f2f2f2,#c9c9c9)"></div><h4>PRODUCT NAME</h4><div class="price">$56.67</div><a class="add" href="#">ADD TO CART</a></div>
    <div class="card"><span class="new">NEW</span><div class="pic" role="img" aria-label="Black bottle filler tool" style="background:linear-gradient(#eee,#2a2a2a)"></div><h4>PRODUCT NAME</h4><div class="price">$56.67</div><a class="add" href="#">ADD TO CART</a></div>
    <div class="card"><div class="pic" role="img" aria-label="Fermentation buckets kit" style="background:linear-gradient(#f4efe6,#c8a06a)"></div><h4>PRODUCT NAME</h4><div class="price">$56.67</div><a class="add" href="#">ADD TO CART</a></div>
    <div class="card"><span class="new">NEW</span><div class="pic" role="img" aria-label="Pump with tubing" style="background:linear-gradient(#f2f2f2,#b33a2e)"></div><h4>PRODUCT NAME</h4><div class="price">$56.67</div><a class="add" href="#">ADD TO CART</a></div>
    <div class="card"><span class="new">NEW</span><div class="pic" role="img" aria-label="Black electric brewing kettle" style="background:linear-gradient(#eee,#1f1f1f)"></div><h4>PRODUCT NAME</h4><div class="price">$56.67</div><a class="add" href="#">ADD TO CART</a></div>
    <div class="card"><div class="pic" role="img" aria-label="Copper wort chiller coil" style="background:linear-gradient(#f5efe6,#b57a3c)"></div><h4>PRODUCT NAME</h4><div class="price">$56.67</div><a class="add" href="#">ADD TO CART</a></div>
    <div class="card"><div class="pic" role="img" aria-label="Stainless steel brewing pot" style="background:linear-gradient(#f5f5f5,#9aa1a8)"></div><h4>PRODUCT NAME</h4><div class="price">$56.67</div><a class="add" href="#">ADD TO CART</a></div>
    <div class="card"><div class="pic" role="img" aria-label="Coloured measuring strips" style="background:linear-gradient(135deg,#f2d94a,#4caf50,#2f6fb7)"></div><h4>PRODUCT NAME</h4><div class="price">$56.67</div><a class="add" href="#">ADD TO CART</a></div>
  </div>
  <div class="pager">
    <span><svg width="10" height="16" viewBox="0 0 10 16"><path d="M8 2L2 8l6 6" fill="none" stroke="#555" stroke-width="2"/></svg></span>
    <span><svg width="10" height="16" viewBox="0 0 10 16"><path d="M2 2l6 6-6 6" fill="none" stroke="#555" stroke-width="2"/></svg></span>
  </div>
</section>

<section class="mailing">
  <h2>JOIN OUR MAILING LIST</h2>
  <input type="email" placeholder="Enter Email">
  <button type="button">SIGN UP</button>
</section>

<footer class="footer">
  <div>
    <h5>CONTACT US</h5>
    <ul>
      <li><svg width="12" height="14" viewBox="0 0 12 16"><path d="M6 0a6 6 0 00-6 6c0 4 6 10 6 10s6-6 6-10a6 6 0 00-6-6z" fill="#0b3566"/></svg><span>Kornlyst Homebrew, Egevej 14<br>4200 Slagelse, Denmark</span></li>
      <li><svg width="12" height="14" viewBox="0 0 24 24"><path d="M6 2l4 4-2 3c1 3 4 6 7 7l3-2 4 4-3 4C10 21 3 14 2 5z" fill="#0b3566"/></svg>Call us - 40 12 34 56</li>
      <li><svg width="12" height="14" viewBox="0 0 24 18"><rect width="24" height="18" rx="2" fill="#0b3566"/><path d="M2 2l10 8 10-8" fill="none" stroke="#fff" stroke-width="2"/></svg>info@kornlyst.dk</li>
    </ul>
  </div>
  <div>
    <h5>CUSTOMER SERVICE</h5>
    <ul><li>Frequently asked questions</li><li>Ordering terms</li><li>Privacy Policy</li><li>Here you find us</li><li>Contact us</li></ul>
  </div>
  <div>
    <h5>INFORMATION</h5>
    <ul><li>Information</li><li>About us</li><li>Fast delivery</li><li>Secure trade</li><li>Instructions</li></ul>
  </div>
  <div>
    <h5>CONNECT WITH US</h5>
    <div class="social"><span></span><span></span><span></span><span></span></div>
  </div>
</footer>

<div class="bottom">
  <span class="paycard"></span><span class="paycard"></span><span class="paycard"></span><span class="paycard"></span><span class="paycard"></span>
  <span class="copy">© copyright 2020 Kornlyst.dk All Rights Reserved | Privacy policy</span>
  <span class="totop"><svg width="16" height="10" viewBox="0 0 16 10"><path d="M2 8l6-6 6 6" fill="none" stroke="#555" stroke-width="2"/></svg></span>
</div>

</body>
</html>
```